Email Banner (QuillStacks)

We require an email banner for our email promotions sent to prospect clients. The banner needs to contain the wording QuillStacks and use the same colour scheme as the logos attached.

This is for B2B professional's so needs to look like a place you would come to read technology articles.

```html
<!DOCTYPE html>
<html lang="en">
<head>
<meta charset="UTF-8">
<title>QuillStacks Email Banners</title>
<link rel="stylesheet" href="https://fonts.googleapis.com/css2?family=Montserrat:wght@400;500&display=swap">
<style>
  :root {
    --stage-dark: #000000;
    --stage-light: #ffffff;
    --navy-deep: #1a1f33;
    --navy-mid: #3a2f4a;
    --plum: #7a2a3a;
    --red-bright: #c8161c;
    --red-deep: #a51218;
    --navy-board: #252c52;
    --red-board: #8a2233;
    --title-white: #ffffff;
  }
  * { margin: 0; padding: 0; box-sizing: border-box; }
  html, body {
    width: 1200px;
    height: 1200px;
    overflow: hidden;
  }
  body {
    font-family: "Montserrat", sans-serif;
  }
  .stage {
    position: relative;
    width: 1200px;
    height: 600px;
  }
  .stage--dark { background: var(--stage-dark); }
  .stage--light { background: var(--stage-light); }
  .banner {
    position: absolute;
    left: 207px;
    top: 223px;
    width: 786px;
    height: 154px;
    display: flex;
    align-items: center;
    justify-content: center;
    overflow: hidden;
  }
  .banner__backdrop {
    position: absolute;
    inset: 0;
  }
  .banner--gradient .banner__backdrop {
    background:
      radial-gradient(ellipse at 85% 20%, rgba(220, 30, 40, 0.6), transparent 55%),
      linear-gradient(90deg, var(--navy-deep) 0%, var(--navy-mid) 25%, var(--plum) 45%, var(--red-deep) 70%, var(--red-bright) 100%);
  }
  .banner--circuit .banner__backdrop {
    background:
      radial-gradient(ellipse at 20% 30%, rgba(200, 30, 45, 0.45), transparent 50%),
      radial-gradient(ellipse at 85% 40%, rgba(200, 30, 45, 0.4), transparent 50%),
      radial-gradient(ellipse at 60% 90%, rgba(180, 30, 45, 0.35), transparent 45%),
      var(--navy-board);
  }
  .banner__title {
    position: relative;
    color: var(--title-white);
    font-family: "Montserrat", sans-serif;
    font-weight: 500;
    font-size: 60px;
    letter-spacing: 0.5px;
    line-height: 1;
  }
</style>
</head>
<body>
  <section class="stage stage--dark">
    <div class="banner banner--gradient">
      <div class="banner__backdrop" role="img" aria-label="Abstract technology backdrop of circuit traces and floating spheres fading from dark navy to bright red"></div>
      <h1 class="banner__title">QuillStacks</h1>
    </div>
  </section>
  <section class="stage stage--light">
    <div class="banner banner--circuit">
      <div class="banner__backdrop" role="img" aria-label="Close-up of a circuit board tinted red on a deep navy background"></div>
      <h2 class="banner__title">QuillStacks</h2>
    </div>
  </section>
</body>
</html>
```